Movrette Business Card

We need a business card design for Movrette, an independent sewing pattern company based near Quebec City. We make patterns for children and adults and specialize in everything other big pattern brands won't tackle: activewear, sportswear (figure skating, gymnastics), underwear. We are a small business and would like our cards to be stylish and fun, not corporate looking.

Target Market(s)

Educated women 35-55 who sew for themselves or their family. They like fashion and sew to be different and make clothes that fit them like a glove, not necessarily to save money.

Industry/Entity Type

Small Business

Requirements
Must have
• Movrette logo, contact info:

Odile Parmont, president & founder / présidente et fondatrice

Movrette
3915 rue Lavoie
St-Romuald QC H2K4P8
Canada

info@movrette.com
www.movrette.com
Nice to have
• Sewing/fashion-related graphics. You can use any pattern cover available on www.movrette.com for inspiration. Stylish illustrations / sketches inspired by existing garments we have would be great. Something showing pattern grading could also be an option.

The design can be on one- or two-sided. We are open to variations (e.g. 4-5 different backs for a given card)
Should not have
• nothing too cartoonish or girly please :) we prefer something timeless, fashion-forward.

```html
<!DOCTYPE html>
<html lang="en">
<head>
<meta charset="utf-8">
<title>Movrette Business Card</title>
<link href="https://fonts.googleapis.com/css2?family=Arimo:wght@400;700&family=Oswald:wght@700&display=swap" rel="stylesheet">
<style>
  :root {
    --page: #e7e4df;
    --denim: #3f5d70;
    --denim-dark: #2a4253;
    --linen: #dcdcdb;
    --linen-dark: #c9c9c8;
    --rust: #c4643b;
    --thread: #e6d8a6;
    --ink: #1d1d1d;
    --slate: #3a4550;
    --light-text: #e9eef1;
  }
  * { margin: 0; padding: 0; box-sizing: border-box; }
  html, body { width: 1200px; height: 900px; overflow: hidden; }
  body { background: var(--page); font-family: "Arimo", Arial, sans-serif; position: relative; }

  .card {
    position: absolute;
    width: 680px;
    height: 388px;
    overflow: hidden;
    box-shadow: 0 6px 18px rgba(0,0,0,.25);
  }
  .card-back { left: 60px; top: 40px; }
  .card-front { left: 460px; top: 472px; }
  .card-art { position: absolute; inset: 0; }

  .rotated { position: absolute; transform-origin: 0 0; white-space: nowrap; }

  /* Front */
  .front-brand {
    left: 98px; top: 14px;
    transform: rotate(60deg);
    display: flex; align-items: center; gap: 10px;
    font-size: 34px; font-weight: 700; color: var(--ink);
  }
  .brand-mark { width: 14px; height: 14px; background: var(--rust); }
  .front-web {
    left: 312px; top: 52px;
    transform: rotate(60deg);
    font-family: "Oswald", "Arial Narrow", sans-serif;
    font-size: 26px; font-weight: 700; color: var(--slate);
    letter-spacing: .5px;
  }
  .contact-block {
    left: 505px; top: 20px;
    transform: rotate(60deg);
    color: var(--light-text);
  }
  .contact-name { font-size: 30px; line-height: 36px; }
  .contact-line { font-size: 16px; line-height: 20px; }

  /* Back */
  .back-brand {
    position: absolute; right: 50px; top: 36px;
    display: flex; align-items: center; gap: 10px;
    font-size: 36px; font-weight: 700; color: var(--light-text);
  }
  .back-brand .brand-mark { background: var(--light-text); }
  .back-web {
    position: absolute; left: 40px; top: 238px;
    font-family: "Oswald", "Arial Narrow", sans-serif;
    font-size: 28px; font-weight: 700; color: var(--slate);
    transform: rotate(4deg); transform-origin: 0 0;
  }
  .tagline {
    position: absolute; right: 36px; top: 282px;
    font-size: 24px; line-height: 28px; color: var(--ink);
    text-align: right;
  }
</style>
</head>
<body>

<section class="card card-back" aria-label="Business card back">
  <svg class="card-art" viewBox="0 0 680 388" width="680" height="388">
    <defs>
      <linearGradient id="denim-back" x1="0" y1="0" x2="1" y2="1">
        <stop offset="0" stop-color="#4a6a7d"/>
        <stop offset="1" stop-color="#2a4253"/>
      </linearGradient>
      <linearGradient id="needle-fill" x1="0" y1="1" x2="1" y2="0">
        <stop offset="0" stop-color="#b9b48a" stop-opacity=".15"/>
        <stop offset="1" stop-color="#d8dde0" stop-opacity=".45"/>
      </linearGradient>
    </defs>
    <rect width="680" height="388" fill="url(#denim-back)"/>
    <polygon points="0,180 680,230 680,388 0,388" fill="var(--linen)"/>
    <line x1="0" y1="190" x2="680" y2="240" stroke="var(--slate)" stroke-width="2" stroke-dasharray="10 6" opacity=".6"/>
    <rect x="90" y="100" width="400" height="60" rx="30" fill="url(#needle-fill)" role="img" aria-label="Illustration of a needle and thread"/>
  </svg>
  <div class="back-brand"><span class="brand-mark"></span>Movrette</div>
  <div class="back-web">WWW.MOVRETTE.COM</div>
  <p class="tagline">The difference between style<br>and fashion is quality.</p>
</section>

<section class="card card-front" aria-label="Business card front">
  <svg class="card-art" viewBox="0 0 680 388" width="680" height="388">
    <defs>
      <linearGradient id="denim-front" x1="0" y1="0" x2="1" y2="1">
        <stop offset="0" stop-color="#4a6a7d"/>
        <stop offset="1" stop-color="#2a4253"/>
      </linearGradient>
      <radialGradient id="scissors-fill">
        <stop offset="0" stop-color="#2a2a2a" stop-opacity=".85"/>
        <stop offset="1" stop-color="#2a2a2a" stop-opacity="0"/>
      </radialGradient>
    </defs>
    <rect width="680" height="388" fill="url(#denim-front)"/>
    <polygon points="0,0 200,0 424,388 0,388" fill="var(--linen)"/>
    <polygon points="200,0 226,0 450,388 424,388" fill="var(--rust)"/>
    <polygon points="226,0 300,0 524,388 450,388" fill="var(--linen-dark)"/>
    <polygon points="300,0 326,0 550,388 524,388" fill="var(--rust)"/>
    <line x1="213" y1="0" x2="437" y2="388" stroke="var(--thread)" stroke-width="2" stroke-dasharray="8 5"/>
    <line x1="313" y1="0" x2="537" y2="388" stroke="var(--thread)" stroke-width="2" stroke-dasharray="8 5"/>
    <line x1="520" y1="10" x2="650" y2="235" stroke="var(--thread)" stroke-width="2" stroke-dasharray="8 5"/>
    <line x1="525" y1="7" x2="655" y2="232" stroke="var(--thread)" stroke-width="2" stroke-dasharray="8 5"/>
    <ellipse cx="120" cy="290" rx="100" ry="80" fill="url(#scissors-fill)" role="img" aria-label="Illustration of open scissors"/>
  </svg>
  <div class="rotated front-brand"><span class="brand-mark"></span>Movrette</div>
  <div class="rotated front-web">WWW.MOVRETTE.COM</div>
  <div class="rotated contact-block">
    <p class="contact-name">Odile Parmont</p>
    <p class="contact-line">president &amp; founder</p>
    <p class="contact-line">présidente et fondatrice</p>
    <p class="contact-line">3915 rue Lavoie St-Romuald</p>
    <p class="contact-line">QC H2K4P8 Canada</p>
    <p class="contact-line">email: info@movrette.com</p>
  </div>
</section>

</body>
</html>
```